BUILT FOR GLORY - SPORTS

Background picture depicting different sports, maybe cycling, running & swimming
My business name is Built for Glory - Sports
SPECIALISING IN MENTAL SPORTS IMAGERY.
SPORTS & REMEDIAL MASSAGE
FLUX CYCLE PRO TRAINING SESSIONS & CUSTOMISED PROGRAMS.
CALL FOR COMPREHENSIVE FREE QUOTE.

CLARA DENTON
0427 318 642
claradenton4@fernmail.net

Target Market(s)

Athletes, mostly cyclists.

Industry/Entity Type

Business

Font styles to use
Script

Colors

Designer to choose colors to be used in the design.

```html
<!DOCTYPE html>
<html lang="en">
<head>
<meta charset="utf-8">
<title>Built for Glory - Sports — Business Card</title>
<link href="https://fonts.googleapis.com/css2?family=Satisfy&family=Dancing+Script:wght@400&family=Open+Sans:wght@400&display=block" rel="stylesheet">
<style>
  :root {
    --stage: #e9e6e2;
    --card: #000000;
    --ink: #ffffff;
    --art-light: #2c2c2c;
    --art-dark: #111111;
  }
  html, body {
    margin: 0;
    width: 1200px;
    height: 871px;
    overflow: hidden;
    background: var(--stage);
  }
  .business-card {
    position: absolute;
    left: 150px;
    top: 178px;
    width: 900px;
    height: 514px;
    overflow: hidden;
    background: var(--card);
    color: var(--ink);
    box-shadow: 0 10px 30px rgba(0,0,0,0.25);
  }
  .brand-name {
    position: absolute;
    right: 60px;
    top: 50px;
    margin: 0;
    font-family: "Satisfy", "Dancing Script", "Brush Script MT", "Segoe Script", cursive;
    font-weight: 400;
    font-style: normal;
    font-size: 58px;
    line-height: 1.2;
    letter-spacing: 1px;
    white-space: nowrap;
  }
  .athletes-art {
    position: absolute;
    left: 70px;
    top: 180px;
    width: 370px;
    height: 290px;
    border-radius: 6px;
    background: radial-gradient(ellipse at center, var(--art-light), var(--art-dark) 75%);
  }
  .contact-list {
    position: absolute;
    left: 500px;
    top: 225px;
    margin: 0;
    padding: 0;
    list-style: none;
    font-family: "Open Sans", "Segoe UI", sans-serif;
    font-weight: 400;
  }
  .contact-item {
    display: flex;
    align-items: center;
    gap: 16px;
    white-space: nowrap;
  }
  .contact-icon { width: 40px; height: 40px; flex: none; }
  .contact-name { font-size: 38px; margin-bottom: 34px; }
  .contact-phone { font-size: 32px; margin-bottom: 38px; margin-left: 14px; }
  .contact-email { font-size: 22px; margin-left: 26px; }
</style>
</head>
<body>
  <section class="business-card">
    <h1 class="brand-name">Built for Glory - Sports</h1>

    <div class="athletes-art" role="img" aria-label="White silhouettes of a cyclist and a runner in motion"></div>

    <ul class="contact-list">
      <li class="contact-item contact-name">
        <svg class="contact-icon" viewBox="0 0 40 40" aria-hidden="true">
          <circle cx="20" cy="20" r="19" fill="#fff"/>
          <circle cx="20" cy="15" r="6" fill="#000"/>
          <path d="M9 30 a11 9 0 0 1 22 0 z" fill="#000"/>
        </svg>
        <span>Clara Denton</span>
      </li>
      <li class="contact-item contact-phone">
        <svg class="contact-icon" viewBox="0 0 40 40" aria-hidden="true">
          <circle cx="20" cy="20" r="19" fill="#fff"/>
          <rect x="13" y="8" width="14" height="24" rx="2.5" fill="none" stroke="#000" stroke-width="2"/>
          <line x1="17" y1="11.5" x2="23" y2="11.5" stroke="#000" stroke-width="1.5"/>
          <circle cx="20" cy="28" r="1.4" fill="#000"/>
        </svg>
        <span>0427 318 642</span>
      </li>
      <li class="contact-item contact-email">
        <svg class="contact-icon" viewBox="0 0 40 40" aria-hidden="true">
          <circle cx="20" cy="20" r="19" fill="#fff"/>
          <rect x="9" y="12" width="22" height="16" fill="none" stroke="#000" stroke-width="2"/>
          <path d="M9 12 L20 21 L31 12" fill="none" stroke="#000" stroke-width="2"/>
        </svg>
        <span>claradenton4@fernmail.net</span>
      </li>
    </ul>
  </section>
</body>
</html>
```